Sleek modern site for stage hypnotist who does high school, college, university and corporate gigs.

Need a website design for stage hypnotist Marcus Wendell
I'm using a weebly domain

Marcus Wendell is a stage hypnotist who does high school shows , colleges, corporate and fundraisers
Looking for something sleek and modern looking.
I need about 4 pages at least one main describing what i do
1st page Describes what events i do (high school, college, corporate, weddings, fundraisers, fairs)
2nd page would be an about/bio page
3rd FAQ page about hypnosis.

*what venues do you work with?
*how long is your show?
*How do we promote the show?
*is it safe
*are you insured?
*how much does it cost?
4th page will be a contact page and link to my social media like Instagram, twitter, and possibly Facebook.

Included is a few pictures that I'll probably including on the site. I'm waiting on the rest for photoshoot at the this week. Some of these pictures probably will have different stock backgrounds other than grey (something like a las vegas strip or a stage.

Visually I'm looking for a cool color scheme.

Target Market(s)

High school for now but college and corporate down the road.

Industry/Entity Type

Entertainment Industry

Coding

Coded - Design and coding required

Number of Pages Required

4 page

Font styles to use
Serif
Sans Serif

Colors
3277b5
85acd3
9d9d9d
5c5c5c
cbcbcb
aaaaaa
1b1b1b
333333

Requirements
Must have
• MUST BE ABLE TO WORK WITH WEEBLY
• A sleek and professional look as if I've been doing this for years.
• The ability to edit the text of the site so i can improve upon the persuasive parts if need be.
• I also will be getting more promotional photos in the 5 or 6 days after the deadline days so if i pick your project i'd like to be able to integrate some of them into the design. The 3 photos i provided are somewhat place holders to give you an idea of the rest that are to come.
Nice to have
• drop down links
Should not have
• if you google other stage hypnotists their sites are a bit stale and not that modern.

```html
<!DOCTYPE html>
<html lang="en">
<head>
<meta charset="utf-8">
<title>Marcus Wendell — Stage Hypnotist</title>
<link href="https://fonts.googleapis.com/css2?family=Montserrat:wght@400;600;700;800&family=Open+Sans:wght@400;600&display=swap" rel="stylesheet">
<style>
:root{
  --ink:#1b1b1b;
  --dark:#333333;
  --grey-bg:#3a3a3a;
  --mid:#5c5c5c;
  --soft:#9d9d9d;
  --light:#cbcbcb;
  --accent:#f7931e;
  --violet:#6a5cff;
  --blue:#3277b5;
  --sky:#85acd3;
  --tile-blue:#4b63f0;
  --tile-purple:#8e3fa3;
  --tile-yellow:#f0c52c;
  --tile-red:#d9433a;
  --tile-green:#6aa842;
  --tile-cyan:#1ea0d8;
  --footer:#1c1a2e;
  --footer-deep:#141222;
}
*{margin:0;padding:0;box-sizing:border-box}
html,body{width:1200px;height:3344px;overflow:hidden}
body{font-family:"Open Sans",Arial,sans-serif;color:var(--dark);background:#fff;position:relative}
h1,h2,h3,h4,.nav,.btn{font-family:"Montserrat",Arial,sans-serif}
section,header,footer{position:absolute;left:0;width:1200px}

/* Hero */
.hero{top:0;height:640px;overflow:hidden}
.hero-photo{position:absolute;inset:0;background:radial-gradient(circle at 30% 40%,#5a4a7a 0%,#2a1f4a 40%,#120e24 80%)}
.nav{position:absolute;top:30px;left:40px;right:40px;display:flex;justify-content:space-between;align-items:center;color:#fff}
.brand{font-size:16px;font-weight:600}
.nav-right{display:flex;gap:18px;align-items:center;font-size:11px;font-weight:700;letter-spacing:1px}
.nav-btn{border:1.5px solid #e04c4c;border-radius:16px;padding:6px 14px}
.hero-circle{position:absolute;left:600px;top:100px;width:460px;height:440px;border-radius:50%;background:rgba(20,16,40,.82);display:flex;flex-direction:column;justify-content:center;padding-left:70px}
.hero-kicker{color:#ddd;font-size:13px;width:300px;margin-bottom:14px}
.hero-title{color:#fff;font-size:30px;font-weight:800;line-height:1.15}
.hero-title span{color:var(--sky)}
.btn{display:inline-block;background:var(--violet);color:#fff;font-size:12px;font-weight:600;padding:10px 28px;border-radius:3px;margin-top:26px;width:max-content}
.hero-arrow{position:absolute;top:290px;width:20px;height:30px}

/* About */
.about{top:640px;height:548px;background:var(--grey-bg);color:#ddd}
.about-text{position:absolute;left:140px;top:110px;width:640px}
.about h2{color:#fff;font-size:30px;font-weight:700;margin-bottom:26px}
.about p{font-size:13px;line-height:1.6;margin-bottom:16px}
.socials{display:flex;gap:14px;margin-top:20px}
.socials i{width:40px;height:40px;border-radius:50%;display:block}
.about-photo{position:absolute;right:0;top:0;width:400px;height:548px;background:linear-gradient(180deg,#4a4a4a,#2b2b2b)}

/* What I do */
.services{top:1188px;height:392px;background:#fff;text-align:center}
.services h2{color:#e8542a;font-size:30px;font-weight:700;margin-top:50px}
.tiles{position:absolute;left:160px;top:120px;width:880px;display:grid;grid-template-columns:repeat(3,280px);gap:20px 20px}
.tile{height:120px;color:#fff;font-family:"Montserrat",Arial,sans-serif;font-size:13px;font-weight:700;text-align:left;padding:80px 0 0 24px}

/* Schedule */
.schedule{top:1580px;height:260px;background:#fff}
.schedule-ghost{position:absolute;top:0;width:100%;text-align:center;font-family:"Montserrat",Arial,sans-serif;font-size:64px;font-weight:800;color:#ececec}
.schedule h2{position:absolute;top:22px;width:100%;text-align:center;font-size:28px;font-weight:700;color:var(--ink)}
.schedule h2 span{color:#e8542a}
.sched-arrow{position:absolute;top:90px;width:40px;height:110px;background:#e6e6e6}
.day-tabs{position:absolute;left:300px;top:90px;width:600px;display:grid;grid-template-columns:repeat(3,180px);gap:10px 20px}
.day{background:#f1f1f1;padding:12px 30px;font-size:11px;color:var(--soft)}
.day b{display:block;font-family:"Montserrat",Arial,sans-serif;font-size:14px;color:var(--ink)}
.day b em{color:#e8542a;font-style:normal}
.day.active{background:var(--accent);color:#fff;margin-top:-12px}
.day.active b{color:#fff}

/* Stats */
.stats{top:1840px;height:240px;background:linear-gradient(90deg,#1d1d24,#2c2a30 50%,#1d1d24)}
.stat-row{position:absolute;top:94px;left:170px;right:170px;display:flex;justify-content:space-between}
.stat{display:flex;align-items:center;gap:14px;color:#fff}
.stat strong{font-family:"Montserrat",Arial,sans-serif;font-size:26px;display:block}
.stat small{font-size:11px;color:var(--light)}

/* Testimonials */
.testimonials{top:2080px;height:560px;background:linear-gradient(180deg,#7a6ea0 0%,#4f77b0 55%,#2f8fc2 100%);text-align:center;color:#fff}
.testimonials h2{font-size:30px;font-weight:700;margin-top:60px}
.quotes{position:absolute;top:160px;left:170px;width:860px;display:grid;grid-template-columns:repeat(3,1fr);gap:40px}
.avatar{width:160px;height:160px;border-radius:50%;border:6px solid #fff;margin:0 auto 30px;background:linear-gradient(135deg,#6bb0c8,#3e6f8a)}
.quote p{font-size:13px;line-height:1.5;margin-bottom:18px}
.quote h4{font-size:13px;font-weight:600}
.quote small{font-size:11px;color:#dbe6f2}

/* CTA */
.cta{top:2640px;height:260px;background:linear-gradient(90deg,#1e1e26,#3a3440 60%,#2a2630);text-align:center;color:#fff}
.cta small{display:block;margin-top:76px;font-size:12px;color:var(--light)}
.cta h2{font-size:30px;font-weight:700;margin:8px 0 14px}
.ghost-btn{display:inline-block;border:1.5px solid #e04c4c;border-radius:16px;padding:6px 20px;font-family:"Montserrat",Arial,sans-serif;font-size:11px;font-weight:700}

/* Footer */
.footer{top:2900px;height:380px;background:var(--footer);color:var(--soft)}
.footer-cols{position:absolute;top:70px;left:160px;right:160px;display:grid;grid-template-columns:300px 220px 200px 1fr}
.footer h3{color:#fff;font-size:32px;font-weight:700;margin-bottom:10px}
.footer h4{color:#fff;font-size:13px;font-weight:600;margin-bottom:16px}
.footer p,.footer li{font-size:11px;line-height:1.7;list-style:none}
.footer p{width:250px}
.subscribe{display:flex;margin-top:12px}
.subscribe span{background:#fff;color:var(--soft);font-size:11px;padding:8px 10px;width:180px}
.subscribe b{background:var(--accent);color:#fff;font-size:11px;padding:8px 12px;font-weight:600}
.bottom-bar{top:3280px;height:64px;background:var(--footer-deep);color:var(--soft);font-size:11px}
.bottom-bar .copy{position:absolute;left:160px;top:25px}
.bottom-bar .dots{position:absolute;right:160px;top:20px;display:flex;gap:10px}
.bottom-bar .dots i{width:22px;height:22px;border-radius:50%;background:#3a3852;display:block}
</style>
</head>
<body>

<header class="hero">
  <div class="hero-photo" role="img" aria-label="Stage hypnotist reaching toward the camera against a starry purple backdrop"></div>
  <nav class="nav">
    <div class="brand">Marcus Wendell</div>
    <div class="nav-right"><span>☰ MENU</span><span class="nav-btn">EVENTS</span></div>
  </nav>
  <svg class="hero-arrow" style="left:20px" viewBox="0 0 20 30"><path d="M15 3 L4 15 L15 27" stroke="#fff" stroke-width="3" fill="none"/></svg>
  <svg class="hero-arrow" style="right:20px" viewBox="0 0 20 30"><path d="M5 3 L16 15 L5 27" stroke="#fff" stroke-width="3" fill="none"/></svg>
  <div class="hero-circle">
    <p class="hero-kicker">A stage that makes room for wonder and endless possibilities.</p>
    <h1 class="hero-title">WHEN <span>IMAGINATION</span><br><span>TAKES SHAPE</span></h1>
    <span class="btn">Read More</span>
  </div>
</header>

<section class="about">
  <div class="about-text">
    <h2>About Finibus Bonorum et Malorum</h2>
    <p>Sed ut perspiciatis unde omnis iste natus error sit voluptatem accusantium doloremque laudantium, totam rem aperiam, eaque ipsa quae ab illo inventore veritatis et quasi architecto beatae vitae dicta sunt explicabo. Nemo enim ipsam voluptatem quia voluptas sit aspernatur aut odit aut fugit, sed quia consequuntur magni dolores eos qui ratione voluptatem sequi nesciunt.</p>
    <p>At vero eos et accusamus et iusto odio dignissimos ducimus qui blanditiis praesentium voluptatum deleniti atque corrupti quos dolores et quas molestias excepturi sint occaecati cupiditate non provident, similique sunt in culpa qui officia deserunt mollitia animi.</p>
    <div class="socials"><i style="background:#f0c52c"></i><i style="background:#3277b5"></i><i style="background:#d9433a"></i></div>
  </div>
  <div class="about-photo" role="img" aria-label="Portrait of the hypnotist in a dark shirt"></div>
</section>

<section class="services">
  <h2>What I DO</h2>
  <div class="tiles">
    <div class="tile" style="background:var(--tile-blue)">HIGH SCHOOL</div>
    <div class="tile" style="background:var(--tile-purple)">COLLEGE</div>
    <div class="tile" style="background:var(--tile-yellow)">CORPORATE</div>
    <div class="tile" style="background:var(--tile-red)">WEDDINGS</div>
    <div class="tile" style="background:var(--tile-green)">FUNDRAISERS</div>
    <div class="tile" style="background:var(--tile-cyan)">FAIRS</div>
  </div>
</section>

<section class="schedule">
  <div class="schedule-ghost">EVENT SCHEDULE</div>
  <h2>Event <span>Schedule</span></h2>
  <div class="sched-arrow" style="left:240px"></div>
  <div class="sched-arrow" style="left:920px"></div>
  <div class="day-tabs">
    <div class="day"><b>DAY <em>01</em></b>21st August 2017</div>
    <div class="day active"><b>DAY 02</b>22nd August 2017</div>
    <div class="day"><b>DAY <em>03</em></b>23rd August 2017</div>
    <div class="day"><b>DAY <em>04</em></b>24th August 2017</div>
  </div>
</section>

<section class="stats" role="img" aria-label="Dim stage crowd backdrop behind show statistics">
  <div class="stat-row">
    <div class="stat"><svg width="40" height="36" viewBox="0 0 40 36"><rect x="2" y="6" width="36" height="28" rx="3" fill="none" stroke="#f7931e" stroke-width="3"/><path d="M2 14h36M11 2v8M29 2v8" stroke="#f7931e" stroke-width="3"/></svg><div><strong>241</strong><small>Useful Sessions</small></div></div>
    <div class="stat"><svg width="36" height="36" viewBox="0 0 36 36"><rect x="12" y="2" width="12" height="20" rx="6" fill="#f7931e"/><path d="M6 18a12 12 0 0 0 24 0M18 30v5" stroke="#f7931e" stroke-width="3" fill="none"/></svg><div><strong>137</strong><small>Great Speakers</small></div></div>
    <div class="stat"><svg width="40" height="36" viewBox="0 0 40 36"><rect x="2" y="6" width="36" height="28" rx="3" fill="none" stroke="#f7931e" stroke-width="3"/><path d="M2 14h36M11 2v8M29 2v8" stroke="#f7931e" stroke-width="3"/></svg><div><strong>241</strong><small>Useful Sessions</small></div></div>
    <div class="stat"><svg width="36" height="36" viewBox="0 0 36 36"><rect x="12" y="2" width="12" height="20" rx="6" fill="#f7931e"/><path d="M6 18a12 12 0 0 0 24 0M18 30v5" stroke="#f7931e" stroke-width="3" fill="none"/></svg><div><strong>137</strong><small>Great Speakers</small></div></div>
  </div>
</section>

<section class="testimonials">
  <h2>What people say</h2>
  <div class="quotes">
    <div class="quote"><div class="avatar" role="img" aria-label="Guest portrait"></div><p>Lorem Ipsum is simply dummy text of the printing and typesetting industry. Lorem Ipsum has been the industry's standard dummy text ever since the 1500s.</p><h4>Nora Castell</h4><small>CEO, Lipsum</small></div>
    <div class="quote"><div class="avatar" role="img" aria-label="Guest portrait"></div><p>Lorem Ipsum is simply dummy text of the printing and typesetting industry. Lorem Ipsum has been the industry's standard dummy text ever since the 1500s.</p><h4>Nora Castell</h4><small>CEO, Lipsum</small></div>
    <div class="quote"><div class="avatar" role="img" aria-label="Guest portrait"></div><p>Lorem Ipsum is simply dummy text of the printing and typesetting industry. Lorem Ipsum has been the industry's standard dummy text ever since the 1500s.</p><h4>Nora Castell</h4><small>CEO, Lipsum</small></div>
  </div>
</section>

<section class="cta" role="img" aria-label="Blurred stage lights backdrop">
  <small>Request your quote now</small>
  <h2>Check Our Events</h2>
  <span class="ghost-btn">EVENTS</span>
</section>

<footer class="footer">
  <div class="footer-cols">
    <div><h3>Logo</h3><p>Bring the magic of the mind to your next event. Shows built for schools, colleges, companies and celebrations of every size, with laughs that stay long after the final bow.</p></div>
    <div><h4>Contact us</h4><ul><li>410 Harbor Lane, Suite 12</li><li>Lakeview, ST 00000</li><li>Phone: (555) 014-2290</li><li>hello@wendellshows.com</li></ul></div>
    <div><h4>Discover</h4><ul><li>About Us</li><li>Our Work</li><li>Events</li><li>Our Team</li></ul></div>
    <div><h4>Subscribe with us</h4><p style="width:200px">Sign up for our mailing list to get latest updates and offers.</p><div class="subscribe"><span>Email Address</span><b>Go</b></div></div>
  </div>
</footer>
<div class="bottom-bar" style="position:absolute;left:0;width:1200px">
  <span class="copy">© Marcus Wendell. All rights reserved</span>
  <div class="dots"><i></i><i></i><i></i><i></i></div>
</div>

</body>
</html>
```